Flyer for 1 day Lean Manufacturing event

I have: 2 sample flyers for the same event, a Word document with the text I would like to use, photos to include. Not all photos need to be included.

I would like a 2 (maybe 1?) page flyer I can use for marketing this and future events. Can be MS Publisher format, or other as preferred - please provide PDF also just in case.

```html
<!DOCTYPE html>
<html lang="en">
<head>
<meta charset="utf-8">
<title>One Day Lean Manufacturing Simulation – Flyer</title>
<link href="https://fonts.googleapis.com/css2?family=Oswald:wght@600;700&family=Roboto:wght@300;400;700&family=Roboto+Condensed:wght@700&family=Poppins:wght@600&family=Libre+Caslon+Text&display=swap" rel="stylesheet">
<style>
  :root{
    --stage:#2b2b2b;
    --paper:#f4f4f4;
    --blue:#2e5fb6;
    --green:#1aa84b;
    --red:#a91f24;
    --orange:#dd5a26;
    --ink:#3d3d3d;
    --body:#4a4a4a;
    --white:#ffffff;
  }
  *{box-sizing:border-box;margin:0;padding:0}
  html,body{width:1200px;height:800px;overflow:hidden;background:var(--stage)}
  .page{position:absolute;top:65px;width:519px;height:670px;background:var(--paper);overflow:hidden;font-family:"Roboto",sans-serif}
  .page--front{left:71px}
  .page--back{left:626px}
  .page svg.bg{position:absolute;inset:0;width:519px;height:670px}
  .abs{position:absolute}

  /* FRONT */
  .title{left:30px;top:20px;font-family:"Oswald",sans-serif;font-weight:700;font-size:31px;line-height:28.5px;color:var(--ink);letter-spacing:-.2px}
  .powered{left:30px;top:128px;font-family:"Roboto Condensed",sans-serif;font-weight:700;font-size:14.5px;color:var(--white)}
  .kicker{left:30px;top:233px;color:var(--white);font-weight:300;font-size:21px;line-height:26px}
  .kicker b{display:block;font-weight:700;font-size:28px;line-height:32px;letter-spacing:-.3px}
  .copy{color:var(--white);font-size:9.6px;line-height:12.2px}
  .copy p{margin-bottom:11px}
  .copy--left{left:30px;top:298px;width:158px}
  .copy--right{left:205px;top:545px;width:172px}
  .social{left:268px;top:636px;display:flex;gap:7px}
  .social span{width:16px;height:16px;border-radius:50%;background:var(--white)}
  .brand{left:420px;top:600px;display:flex;align-items:center;gap:5px;font-family:"Roboto",sans-serif;font-weight:700;font-size:13px;color:var(--blue)}
  .brand i{width:14px;height:14px;background:var(--green);display:block}

  /* BACK */
  .cover-head{left:24px;top:18px;font-family:"Poppins",sans-serif;font-weight:600;font-size:18.5px;line-height:23px;color:var(--white)}
  .intro{left:263px;top:18px;width:242px;font-size:8.7px;line-height:11.2px;color:var(--body)}
  .intro p{margin-bottom:4px}
  b{font-weight:700;color:#2f2f2f}
  .ticks{list-style:none;font-size:8.7px;line-height:11.2px;color:var(--body)}
  .ticks li{position:relative;padding-left:14px;margin-bottom:11px}
  .ticks li.plain{margin-top:-6px}
  .ticks li:not(.plain)::before{content:"";position:absolute;left:0;top:2px;width:8px;height:8px;border-radius:50%;background:var(--orange)}
  .ticks li:not(.plain)::after{content:"";position:absolute;left:2.5px;top:3.6px;width:2.5px;height:4px;border:solid var(--white);border-width:0 1.2px 1.2px 0;transform:rotate(40deg)}
  .ticks--left{left:24px;top:146px;width:222px}
  .ticks--right{left:260px;top:146px;width:230px}
  .name{left:28px;top:520px;font-family:"Libre Caslon Text",serif;font-size:15.5px;color:var(--white)}
  .bio{color:var(--white);font-size:8.7px;line-height:11.2px}
  .bio p{margin-bottom:8px}
  .bio--side{left:147px;top:408px;width:112px}
  .bio--full{left:28px;top:552px;width:226px}
  .register{left:310px;top:447px;width:37px;height:209px;display:flex;align-items:center;justify-content:center}
  .register span{transform:rotate(-90deg);white-space:nowrap;font-family:"Roboto Condensed",sans-serif;font-weight:700;font-size:21px;color:var(--white);letter-spacing:.5px}
  .details{left:361px;top:458px;width:152px;font-family:"Roboto Condensed",sans-serif;font-weight:700;font-size:8.6px;line-height:11px;color:#333}
  .detail{position:relative;padding-left:20px;padding-bottom:6px;margin-bottom:6px;border-bottom:1px dashed #b9b9b9}
  .detail:last-child{border-bottom:0}
  .detail .lbl{color:var(--orange)}
  .detail svg{position:absolute;left:2px;top:2px;width:13px;height:13px}
</style>
</head>
<body>

<!-- FRONT PAGE -->
<section class="page page--front">
  <svg class="bg" viewBox="0 0 519 670" aria-hidden="false">
    <polygon points="0,151 210,151 210,280 519,420 519,670 0,670" fill="var(--blue)"/>
    <polygon points="0,120 214,120 214,151 0,151" fill="var(--green)"/>
    <polygon points="370,355 519,285 519,440" fill="#2f7a45" role="img" aria-label="Green-tinted photo of participants at work tables"/>
    <polygon points="368,2 518,88.5 518,261.5 368,348 218,261.5 218,88.5" fill="var(--red)"/>
    <defs>
      <linearGradient id="groupPhoto" x1="0" y1="0" x2="1" y2="1">
        <stop offset="0" stop-color="#c9c4bd"/><stop offset=".5" stop-color="#b7643e"/><stop offset="1" stop-color="#4b4f57"/>
      </linearGradient>
      <linearGradient id="bricksPhoto" x1="0" y1="0" x2="1" y2="1">
        <stop offset="0" stop-color="#d9d6d2"/><stop offset=".55" stop-color="#8e8a86"/><stop offset="1" stop-color="#4a4646"/>
      </linearGradient>
      <linearGradient id="portrait" x1="0" y1="0" x2="0" y2="1">
        <stop offset="0" stop-color="#d7d5d0"/><stop offset="1" stop-color="#4b4e56"/>
      </linearGradient>
    </defs>
    <polygon points="368,23 499.6,99 499.6,251 368,327 236.4,251 236.4,99" fill="url(#groupPhoto)" role="img" aria-label="Photo of workshop participants assembling building-block products around a long table"/>
    <polygon points="289,328 381.7,381.5 381.7,488.5 289,542 196.3,488.5 196.3,381.5" fill="var(--orange)"/>
    <polygon points="289,345 367,390 367,480 289,525 211,480 211,390" fill="url(#bricksPhoto)" role="img" aria-label="Photo of two baskets filled with coloured building bricks"/>
    <polygon points="427,568 519,568 519,670 330,670" fill="var(--paper)"/>
  </svg>

  <h1 class="abs title">ONE DAY LEAN<br>MANUFACTURING<br>SIMULATION</h1>
  <div class="abs powered">POWERED BY LEAN CREW</div>
  <div class="abs kicker">Start the year<b>with a bang!</b></div>
  <div class="abs copy copy--left">
    <p>Our one day Lean and TOC Simulation shows you how to integrate Lean into your process, and demonstrates how you can lead or support successful implementation.</p>
    <p style="margin-top:18px">The Simulation uses Lean manufacturing principles to work towards perfecting manufacturing processes. An analysis of the material and information flow leads to the elimination of non-value adding activities, elevating a "typical" production environment to best practice. The immersive nature of the Simulation results in a much deeper and long lasting understanding of the principles of Lean. These principles work in companies regardless of size or sector.</p>
    <p>The Simulation recreates the manufacturing environment through the hands-on assembly of "products" at separate work stations and all participants work together to refine the process and achieve optimum output. (Challenge: try to beat the standing record)</p>
  </div>
  <div class="abs copy copy--right">
    <p>By applying best practice techniques under practical conditions, participants will accelerate awareness and understanding that will enhance the success rate and effectiveness of your Lean program.</p>
  </div>
  <div class="abs social" aria-label="Social links"><span></span><span></span><span></span><span></span><span></span></div>
  <div class="abs brand"><i></i>Lean Crew</div>
</section>

<!-- BACK PAGE -->
<section class="page page--back">
  <svg class="bg" viewBox="0 0 519 670">
    <polygon points="0,0 239,0 239,63 124,122 0,122" fill="var(--green)"/>
    <polygon points="519,287 519,386 375,386" fill="var(--blue)"/>
    <rect x="0" y="377" width="374" height="3" fill="var(--orange)"/>
    <rect x="0" y="386" width="519" height="284" fill="var(--blue)"/>
    <polygon points="425,435 519,376 519,440" fill="#2f7a45" role="img" aria-label="Green-tinted photo of the workshop"/>
    <polygon points="450,372 280,467 280,670 519,670 519,410" fill="var(--red)"/>
    <polygon points="450,393 298,478 298,670 519,670 519,432" fill="var(--white)"/>
    <rect x="310" y="447" width="37" height="209" fill="var(--orange)"/>
    <polygon points="82,402 133,431.5 133,490.5 82,520 31,490.5 31,431.5" fill="var(--green)"/>
    <polygon points="82,411 125.3,436 125.3,486 82,511 38.7,486 38.7,436" fill="url(#portrait)" role="img" aria-label="Portrait photo of the presenter"/>
  </svg>

  <h2 class="abs cover-head">What will be covered<br>and what you will<br>take away</h2>
  <div class="abs intro">
    <p>How to rate your company using a <b>Manufacturing Excellence model,</b> and use the model to drive improvement.</p>
    <p>How to maximise productivity using the <b>Theory of Constraints.</b></p>
    <p>The application of lean methodologies across manufacturing, financials, administration and the supply chain.</p>
    <p>Ability to <b>develop people</b> into a cohesive, flexible, and empowered autonomous team to achieve a common goal of improved performance.</p>
  </div>

  <ul class="abs ticks ticks--left">
    <li>Ability to list, discuss and review process issues by using basic <b>problem solving techniques</b></li>
    <li class="plain">How to identify and <b>eliminate non-value added</b> activities.</li>
    <li>How to distinguish between push and <b>pull systems</b> and understand the control method of <b>Kanban</b> pull signals to balance supply and demand, improve lead times and reduce work-in progress.</li>
    <li>Understand why, when, and how to practice <b>set up time reduction.</b></li>
    <li>Why large <b>batch sizes</b> are not cost effective and increase inventory, lead times, and reduce flexibility.</li>
    <li>Why consistent processes give quality results through <b>standard work</b> practices and procedures.</li>
  </ul>
  <ul class="abs ticks ticks--right">
    <li>The importance of <b>visual performance measures</b> in driving behaviours.</li>
    <li>How the implementation of <b>5S housekeeping</b> is the cornerstone of best practice.</li>
    <li>The importance of quality at source and <b>mistake proofing.</b></li>
    <li>Why <b>preventative and autonomous maintenance</b> is critical to overall equipment effectiveness.</li>
    <li>Understand the key best practices areas of: <b>Leading and Managing Change, Teamwork, Set-up Reduction, Process and Material Flow, Focused Improvement, 5S, and Visual Performance Measures.</b></li>
  </ul>

  <div class="abs name">Daniel Harlow</div>
  <div class="abs bio bio--side">
    <p>is a skilled consultant, specialising in maximising profit, capacity and unlocking production efficiency.</p>
    <p>He is a professional engineer with 18 years of consulting experience in production system design, continuous improvement tools and rapid interventions.</p>
  </div>
  <div class="abs bio bio--full">
    <p>Prior to entering consulting he gained wide-ranging experience in the Australian automotive industry implementing Lean and other World Class practices across the supply chain including Parts and Accessory, Tier 1 Supply, and Vehicle Assembly Plant. He is also a specialist in Inventory Optimisation, Energy Optimisation, Excel Auditing, and the Supply Chain Operations Reference (SCOR) Model</p>
  </div>

  <div class="abs register"><span>REGISTER HERE</span></div>
  <div class="abs details">
    <div class="detail">
      <svg viewBox="0 0 14 14" fill="none" stroke="var(--orange)" stroke-width="1"><rect x="1.5" y="2.5" width="11" height="10" rx="1"/><line x1="1.5" y1="5.5" x2="12.5" y2="5.5"/><line x1="4.5" y1="1" x2="4.5" y2="3.5"/><line x1="9.5" y1="1" x2="9.5" y2="3.5"/></svg>
      <div class="lbl">Date:</div>Friday 16th February 2024
    </div>
    <div class="detail">
      <svg viewBox="0 0 14 14" fill="none" stroke="var(--orange)" stroke-width="1"><circle cx="7" cy="7" r="5.5"/><polyline points="7,3.5 7,7 9.5,8.5"/></svg>
      <div class="lbl">Time:</div>8am to 5pm
    </div>
    <div class="detail">
      <svg viewBox="0 0 14 14" fill="none" stroke="var(--orange)" stroke-width="1"><path d="M2 10h10M3 10a4 4 0 0 1 8 0M7 4.5v1.5M1 12h12"/></svg>
      <div class="lbl">Catering provided</div>
    </div>
    <div class="detail">
      <svg viewBox="0 0 14 14" fill="none" stroke="var(--orange)" stroke-width="1"><path d="M7 13s4.5-4.2 4.5-7.5a4.5 4.5 0 0 0-9 0C2.5 8.8 7 13 7 13z"/><circle cx="7" cy="5.5" r="1.6"/></svg>
      <div class="lbl">Venue:</div>Riverbend Hotel, Garden Room<br>12 Example Parade<br>Brookvale QLD 4000
    </div>
    <div class="detail">
      <svg viewBox="0 0 14 14" fill="none" stroke="var(--orange)" stroke-width="1"><circle cx="7" cy="5" r="3.5"/><path d="M1 12h4l2-1.5h4"/><text x="5.4" y="6.8" font-size="5" fill="var(--orange)" stroke="none">$</text></svg>
      <div class="lbl">Cost:</div>$350 per person incl GST
    </div>
  </div>
</section>

</body>
</html>
```